Simple proffessional BC

I have a logo which I will attach below.
I would like the logo on the front of the card with these details in point form below:
Pre and Post Natal Yoga: Pregnancy Workshops: Hypnobirthing Courses
On the back of the card my details:
Merrin Galvey
Facebook page- calmbellieswillowharbour
Mobile- 0438 512 740

I like the idea of the card being simple, possibly just the above on a plain coloured (eggshell?) card, a card that is textured.
I am open to suggestion if it appeals!
Thank you and good luck!

Target Market(s)

Pregnant women, 20's-40's

Requirements
Must have
• Simple, compliment logo.
Make logo the feature.
Should not have

• .

```html
<!DOCTYPE html>
<html lang="en">
<head>
<meta charset="utf-8">
<title>Calm Bellies – Business Card</title>
<link rel="stylesheet" href="https://fonts.googleapis.com/css2?family=Questrial&display=swap">
<style>
  :root {
    --page-bg: #e4e1da;
    --card-bg: #f7f4dd;
    --card-edge: #e3dfc4;
    --brand-red: #8a1c2c;
    --brand-orange: #eea640;
    --brand-orange-deep: #e08e2c;
    --ink: #2a2624;
  }
  * { box-sizing: border-box; margin: 0; padding: 0; }
  html, body {
    width: 1200px;
    height: 800px;
    overflow: hidden;
    background: var(--page-bg);
    font-family: "Questrial", "Century Gothic", sans-serif;
  }
  .sheet {
    width: 1200px;
    height: 800px;
    display: flex;
    align-items: center;
    justify-content: center;
    gap: 40px;
  }
  .card {
    position: relative;
    width: 540px;
    height: 310px;
    background: var(--card-bg);
    border: 1px solid var(--card-edge);
    box-shadow: 0 10px 26px rgba(0,0,0,0.12);
  }

  /* Front */
  .brand-name {
    position: absolute;
    left: 38px;
    top: 30px;
    font-size: 54px;
    font-weight: 400;
    color: var(--brand-red);
    letter-spacing: 0.5px;
    line-height: 1;
  }
  .brand-mark {
    position: absolute;
    left: 62px;
    top: 122px;
    width: 144px;
    height: 144px;
  }
  .services {
    position: absolute;
    left: 232px;
    top: 112px;
    list-style: none;
  }
  .services li {
    position: relative;
    padding-left: 20px;
    margin-bottom: 30px;
    font-size: 17px;
    color: var(--brand-red);
  }
  .services li:nth-child(2) { margin-left: 8px; }
  .services li:nth-child(3) { margin-left: 16px; }
  .services li::before {
    content: "";
    position: absolute;
    left: 0;
    top: 7px;
    width: 6px;
    height: 6px;
    border-radius: 50%;
    background: var(--brand-orange);
  }

  /* Back */
  .card-back .contact {
    position: absolute;
    left: 52px;
    top: 70px;
  }
  .owner-name {
    font-size: 36px;
    color: var(--ink);
    line-height: 1.1;
  }
  .owner-brand {
    margin-top: 4px;
    margin-left: 40px;
    font-size: 20px;
    color: var(--brand-red);
  }
  .contact-lines {
    margin-top: 40px;
    list-style: none;
    font-size: 20px;
    color: var(--ink);
  }
  .contact-lines li { margin-bottom: 10px; }
</style>
</head>
<body>
<main class="sheet">
  <section class="card card-front" aria-label="Card front">
    <h1 class="brand-name">Calm Bellies</h1>
    <svg class="brand-mark" viewBox="0 0 144 144" aria-hidden="true">
      <defs>
        <radialGradient id="markFill" cx="45%" cy="40%" r="60%">
          <stop offset="0%" stop-color="var(--brand-orange)"/>
          <stop offset="100%" stop-color="var(--brand-orange-deep)"/>
        </radialGradient>
      </defs>
      <circle cx="72" cy="72" r="72" fill="url(#markFill)"/>
    </svg>
    <ul class="services">
      <li>Pre and Post Natal Yoga</li>
      <li>Pregnancy Workshops</li>
      <li>Hypnobirthing Courses</li>
    </ul>
  </section>

  <section class="card card-back" aria-label="Card back">
    <div class="contact">
      <p class="owner-name">Merrin Galvey</p>
      <p class="owner-brand">Calm Bellies</p>
      <ul class="contact-lines">
        <li>0438 512 740</li>
        <li>calmbellieswillowharbour</li>
      </ul>
    </div>
  </section>
</main>
</body>
</html>
```